Business Card Design Project

Our logo/name is trademarked (since around 2000) and is owned by us. Logo originally designed in 1984 by my wife. Our logo needs freshening up while retaining its recognizability and trademark coverage. Our business cards, line card etc., web page home also need freshening, maybe as simple as inserting the updated logo, or completely redesigned.

Our logo represents "torque", which is defined as a force around an axis or "twist". Since 1949, we have been one of the world leaders in Norlane industrial clutches and brakes sales and service. We specialize in heavy duty applications such as stamping presses, steel mills, paper mills, drilling rigs etc. We are engineers as well as business people. Our customers are maintenance supervisors, plant engineers, small business owners. Our "color" has been reflex blue For more background, our website is www.brindlemark-co.com
Updates

I have posted a correct scan of the card/logo front and some previous versions of our logo.  (For now skip the back.)

As my brief said, we are after refreshing the logo and our cards/literature but the logo and card first.

Project Deadline Extended
Reason: I had trouble getting my existing logo scanned. should be up now.

Hopefully, the third try loading my existing logo and card worked!  The "City" banner had been on the0 bottom of the card.

Alt. A:  leave cities off
Alt B.  Instead of the cities, take a look at our web site home page or second page showing the world map and see if the world (as a territory which we do ship worldwide) could be worked in or highlight the back of the
 card with lines and the world? 

Future project will be line card redesign and web site
with separate project budget etc.www.brindlemark-co.com

Project Deadline Extended
Reason: My business partner was out of town last week and I wanted a couple days for his input. Thank you for your patience

Thank you all for your input! Dale Hurst

Target Market(s)

factory maintenance managers, plant engineers, small business owners

Industry/Entity Type

Small Business

Requirements
Must have
• clear development of existing trademarked logo

```html
<!DOCTYPE html>
<html lang="en">
<head>
<meta charset="utf-8">
<title>Brindlemark Co. — Business Card</title>
<link href="https://fonts.googleapis.com/css2?family=Roboto:wght@400;700;900&display=swap" rel="stylesheet">
<style>
  :root {
    --reflex-blue: #0f72c0;
    --blue-light: #2aa3df;
    --ink-dark: #333333;
    --band-dark: #3a3a3a;
    --band-mid: #5a5a5a;
    --paper: #ffffff;
    --paper-grey: #e6e7e9;
    --page-bg: #f3f3f3;
    --text-light: #f4f4f4;
  }
  * { margin: 0; padding: 0; box-sizing: border-box; }
  html, body {
    width: 1200px; height: 900px; overflow: hidden;
    background: var(--page-bg);
    font-family: "Roboto", Arial, sans-serif;
  }
  .canvas { position: relative; width: 1200px; height: 900px; }

  .brand-lockup {
    position: absolute; top: 95px; left: 0; width: 1200px;
    display: flex; justify-content: center; align-items: center; gap: 22px;
  }
  .brand-lockup .brand-name {
    font-weight: 900; font-size: 72px; letter-spacing: 1px;
    color: var(--ink-dark); text-transform: uppercase;
  }
  .brand-lockup .brand-dot {
    width: 96px; height: 96px; border-radius: 50%;
    border: 9px solid var(--reflex-blue);
  }

  .business-card {
    position: absolute; left: 250px; top: 390px;
    width: 700px; height: 400px;
    background: var(--paper);
    box-shadow: 0 12px 30px rgba(0,0,0,0.18);
    overflow: hidden;
  }
  .business-card svg { position: absolute; inset: 0; }

  .card-brand {
    position: absolute; left: 46px; top: 52px;
    display: flex; align-items: center; gap: 14px;
  }
  .card-brand .brand-name {
    font-weight: 900; font-size: 38px; color: var(--paper);
    text-transform: uppercase; letter-spacing: 0.5px;
  }
  .card-brand .brand-dot {
    width: 50px; height: 50px; border-radius: 50%;
    border: 5px solid var(--paper);
  }

  .card-holder {
    position: absolute; left: 0; width: 700px; top: 205px;
    text-align: center; color: var(--reflex-blue);
  }
  .card-holder .holder-name { font-weight: 900; font-size: 30px; letter-spacing: 0.5px; }
  .card-holder .holder-title { font-weight: 400; font-size: 19px; letter-spacing: 1.5px; margin-left: 4px; }

  .card-contact {
    position: absolute; top: 312px; color: var(--text-light);
    font-size: 17px; line-height: 24px;
  }
  .card-contact.address { left: 40px; }
  .card-contact.lines { left: 420px; top: 300px; font-size: 16px; line-height: 23px; }
</style>
</head>
<body>
<main class="canvas">
  <header class="brand-lockup">
    <span class="brand-name">Brindlemark Co.</span>
    <span class="brand-dot" aria-hidden="true"></span>
  </header>

  <section class="business-card" aria-label="Business card">
    <svg width="700" height="400" viewBox="0 0 700 400" aria-hidden="true">
      <defs>
        <linearGradient id="blueBand" x1="0" y1="0" x2="1" y2="0">
          <stop offset="0" stop-color="var(--blue-light)"/>
          <stop offset="1" stop-color="var(--reflex-blue)"/>
        </linearGradient>
        <linearGradient id="paperFade" x1="0" y1="0" x2="1" y2="0">
          <stop offset="0" stop-color="#ffffff"/>
          <stop offset="1" stop-color="var(--paper-grey)"/>
        </linearGradient>
        <linearGradient id="darkBand" x1="0" y1="0" x2="0" y2="1">
          <stop offset="0" stop-color="var(--band-mid)"/>
          <stop offset="1" stop-color="var(--band-dark)"/>
        </linearGradient>
      </defs>
      <rect width="700" height="400" fill="url(#paperFade)"/>
      <path d="M0 0 H505 C498 55 492 100 480 122 C340 140 170 150 0 152 Z" fill="url(#blueBand)"/>
      <path d="M0 168 C200 165 420 150 700 120" fill="none" stroke="var(--reflex-blue)" stroke-width="2"/>
      <path d="M520 0 V110 L690 78 V0" fill="none" stroke="var(--reflex-blue)" stroke-width="1.5"/>
      <path d="M505 122 L700 90" fill="none" stroke="var(--reflex-blue)" stroke-width="1"/>
      <path d="M0 290 C220 262 470 244 700 236" fill="none" stroke="#9a9a9a" stroke-width="1.5"/>
      <path d="M0 300 C230 272 470 256 700 250 V400 H0 Z" fill="url(#darkBand)"/>
    </svg>

    <div class="card-brand">
      <span class="brand-name">Brindlemark Co.</span>
      <span class="brand-dot" aria-hidden="true"></span>
    </div>

    <p class="card-holder">
      <span class="holder-name">DALE HURST /</span>
      <span class="holder-title">PRESIDENT</span>
    </p>

    <address class="card-contact address" style="font-style:normal">
      2280 N. Harlow Ridge, Suite 110<br>
      Elmcrest, MI 48390-1204<br>
      E-mail: dhurst@brindlemark-co.com
    </address>

    <p class="card-contact lines">
      Phone (555) 014-9600<br>
      Fax (555) 014-5616<br>
      Parts Hot Line (800) 555-0192
    </p>
  </section>
</main>
</body>
</html>
```